依頼詳細
PC版のTOPページと下層1ページ(採用情報)のデザイン制作をお願いいたします。
サイトマップ、依頼内容詳細.txtをご確認いただき、動画のテイストを参考にシンプルで見やすいデザインで制作いただきたいです。
スムーズな連絡と軽微な修正にご対応いただける方へご依頼をさせていただきたいです。
ターゲットは木材資材・建築資材・家具建具資材などを必要とする建築会社様、家具・建具製造会社様などです。
ページ数
2ページ
希望イメージ
シンプル 複雑
単色 カラフル
暗い 明るい
日常 高級
遊び心 厳粛
未来的 伝統的
女性的 男性的
希望する色
茶系、緑系、グレー系
納品ファイル
• イラストレーター形式 (.ai)
補足説明
納品ファイルはXDも可です。
添付してあるアニメーションにテイストを合わせ、
木の温かみを感じさせるデザインで制作してください。
コーポレートですが、あまり堅くなり過ぎないようにしたいです。
BtoB向けの会社ではありますが、就職などを考えている若い方が見ても、
面白そうな企業だなという印象も与えたいです。
動画ダウンロードURLを新たに添付いたしましたので
そちらからダウンロードをお願い致します。
■ 選んだ理由

爽やかな緑を使ったデザインが良かったです。

■ 提案者全員のお礼・コメント

たくさんのご提案をいただきありがとうございました。

```html
<!DOCTYPE html>
<html lang="ja">
<head>
<meta charset="utf-8">
<title>青葉木材株式会社</title>
<link href="https://fonts.googleapis.com/css2?family=Noto+Sans+JP:wght@400;500;700&family=Montserrat:wght@400;500&display=swap" rel="stylesheet">
<style>
:root{
  --bg:#262626;
  --bg-dark:#1f1f1f;
  --panel:#444444;
  --line:#5a5a5a;
  --text:#ffffff;
  --muted:#bdbdbd;
  --wood-a:#c9a57a;
  --wood-b:#7d5d3e;
}
*{margin:0;padding:0;box-sizing:border-box}
html,body{width:1200px;height:2936px;overflow:hidden}
body{background:var(--bg);color:var(--text);font-family:"Noto Sans JP",sans-serif;position:relative}
.abs{position:absolute}
.en{font-family:"Montserrat",sans-serif}

.header{left:0;top:0;width:1200px;height:180px;background:var(--bg-dark)}
.brand{left:80px;top:40px;display:flex;align-items:center;gap:16px}
.brand-mark{width:40px;height:40px;border:2px solid var(--text)}
.brand-name{font-size:18px;font-weight:500;letter-spacing:.1em}
.nav{right:60px;top:56px;display:flex;gap:0}
.nav a{color:var(--text);text-decoration:none;font-size:14px;padding:6px 22px;border-left:1px solid var(--line)}
.nav a:last-child{border-right:1px solid var(--line)}

.hero-photo{left:0;top:180px;width:900px;height:500px;background:linear-gradient(135deg,var(--wood-a),#a88560 45%,var(--wood-b))}
.hero-copy{left:700px;top:360px;font-size:64px;font-weight:700;line-height:1.45;letter-spacing:.18em}

.section-label{left:80px;font-size:16px;display:flex;align-items:center;gap:16px}
.section-label small{font-family:"Montserrat",sans-serif;font-size:10px;letter-spacing:.15em;color:var(--muted)}

.btn{display:block;width:170px;height:44px;border:1px solid var(--muted);font-family:"Montserrat",sans-serif;font-size:11px;letter-spacing:.15em;text-align:center;line-height:42px;color:var(--text);text-decoration:none}

.about-panel{left:240px;top:760px;width:900px;height:340px;background:var(--panel)}
.about-title{left:290px;top:800px;font-size:34px;font-weight:500;line-height:1.6;letter-spacing:.08em}
.about-body{left:290px;top:950px;font-size:13px;line-height:2.3;color:var(--muted)}

.news-list{left:240px;top:1240px;width:900px;border-top:1px solid var(--line)}
.news-item{border-bottom:1px solid var(--line);padding:18px 0 20px}
.news-item time{display:block;font-family:"Montserrat",sans-serif;font-size:11px;color:var(--muted);margin-bottom:6px}
.news-item p{font-size:14px}

.business-bg{left:0;top:1580px;width:1200px;height:480px;background:linear-gradient(180deg,#2c2c2c,#232323)}
.card{width:240px}
.card-photo{width:240px;height:120px}
.card h3{font-size:15px;font-weight:500;margin:22px 0 14px}
.card p{font-size:11px;color:var(--muted);line-height:1.8;margin-bottom:24px}
.card .btn{width:240px}

.recruit-photo{left:760px;top:2060px;width:440px;height:400px;background:linear-gradient(160deg,#eef0f2,#c7ccd2 60%,#9aa1a8)}
.recruit-title{left:280px;top:2100px;font-size:40px;font-weight:700;line-height:1.6;letter-spacing:.08em}
.recruit-body{left:280px;top:2240px;font-size:13px;line-height:2.2;color:var(--muted)}

.contact{left:0;top:2480px;width:1200px;height:200px;border-top:1px solid var(--line)}
.contact-lead{left:380px;top:2570px;font-size:12px;color:var(--muted)}
.contact-tel{left:380px;top:2592px;font-size:24px;letter-spacing:.04em;display:flex;align-items:center;gap:8px;white-space:nowrap}

.footer{left:0;top:2720px;width:1200px;height:216px;background:var(--bg-dark);text-align:center}
.footer .brand{position:static;justify-content:center;margin-top:40px}
.copyright{font-family:"Montserrat",sans-serif;font-size:10px;color:var(--muted);margin-top:30px;letter-spacing:.1em}
</style>
</head>
<body>

<header class="abs header">
  <div class="abs brand"><span class="brand-mark"></span><span class="brand-name">青葉木材株式会社</span></div>
  <nav class="abs nav">
    <a href="#">ご挨拶</a><a href="#">新着情報</a><a href="#">事業内容</a><a href="#">採用情報</a><a href="#">会社概要</a><a href="#">お問い合わせ</a>
  </nav>
</header>

<div class="abs hero-photo" role="img" aria-label="積み重ねた木材の断面の写真"></div>
<h1 class="abs hero-copy">環境に優しい<br>技術の確立。</h1>

<div class="abs section-label" style="top:800px">ご挨拶<small>GREETING</small></div>
<div class="abs about-panel"></div>
<h2 class="abs about-title">高収益型企業をめざし、<br>成長し続けてまいります。</h2>
<p class="abs about-body">私たちは木材の魅力を活かし、地域とともに歩み続けます。<br>製品づくりを通じて人と自然をつなぎ、暮らしを支える会社を目指します。<br>新しい挑戦を重ね、未来へ価値を届けてまいります。</p>
<a class="abs btn" href="#" style="left:910px;top:1030px">MORE DETAIL</a>

<div class="abs section-label" style="top:1220px">新着情報<small>INFORMATION</small></div>
<div class="abs news-list">
  <div class="news-item"><time>2021.04.01</time><p>会社概要を更新しました</p></div>
  <div class="news-item"><time>2021.03.15</time><p>採用情報を公開しました</p></div>
  <div class="news-item"><time>2021.02.10</time><p>通販サイト「KIBA SHOP」を、「WOODY LIFE STORE」として、新たに公開しました</p></div>
</div>
<a class="abs btn" href="#" style="left:910px;top:1480px">MORE DETAIL</a>

<div class="abs business-bg" role="img" aria-label="薄い線で描かれた地図模様の背景"></div>
<div class="abs section-label" style="top:1660px">事業内容<small>PRODUCT</small></div>
<div class="abs card" style="left:280px;top:1660px">
  <div class="card-photo" role="img" aria-label="積まれた丸太の写真" style="background:linear-gradient(135deg,#b78b5c,#6f4f33)"></div>
  <h3>木材資材</h3><p>国産材を中心に、用途に合わせた木材をお届けします。</p>
  <a class="btn" href="#">MORE DETAIL</a>
</div>
<div class="abs card" style="left:560px;top:1660px">
  <div class="card-photo" role="img" aria-label="建築中の木造住宅の写真" style="background:linear-gradient(135deg,#9cc3e0,#c59a6a)"></div>
  <h3>建築資材</h3><p>住まいづくりを支える、確かな品質の資材を提供します。</p>
  <a class="btn" href="#">MORE DETAIL</a>
</div>
<div class="abs card" style="left:832px;top:1660px">
  <div class="card-photo" role="img" aria-label="家具建具用の木材部材の写真" style="background:linear-gradient(135deg,#e3d3bd,#a78460)"></div>
  <h3>家具建具資材</h3><p>家具や建具の製造に最適な、加工用の材料をご用意します。</p>
  <a class="btn" href="#">MORE DETAIL</a>
</div>

<div class="abs section-label" style="top:2120px">採用情報<small>RECRUIT</small></div>
<h2 class="abs recruit-title">社会を変える最前線で、<br>心躍る仕事を。</h2>
<p class="abs recruit-body">木の魅力を伝える仕事に、あなたの力を活かしませんか。<br>若い世代が活躍できる環境で、ともに未来をつくりましょう。<br>新しい仲間との出会いを楽しみにしています。</p>
<a class="abs btn" href="#" style="left:280px;top:2340px">MORE DETAIL</a>
<div class="abs recruit-photo" role="img" aria-label="明るいオフィスを行き交う人々の写真"></div>

<div class="abs contact"></div>
<div class="abs section-label" style="top:2592px">お問い合わせ<small>CONTACT</small></div>
<p class="abs contact-lead">お電話でのお問い合わせはこちらから</p>
<div class="abs contact-tel en">
  <svg width="20" height="20" viewBox="0 0 24 24" fill="#fff"><path d="M6.6 10.8a15.1 15.1 0 0 0 6.6 6.6l2.2-2.2c.3-.3.7-.4 1-.2 1.1.4 2.3.6 3.6.6.6 0 1 .4 1 1V20c0 .6-.4 1-1 1A17 17 0 0 1 3 4c0-.6.4-1 1-1h3.5c.6 0 1 .4 1 1 0 1.3.2 2.5.6 3.6.1.3 0 .7-.2 1z"/></svg>
  011-555-0142
</div>
<a class="abs btn" href="#" style="left:640px;top:2580px;width:212px">CONTACT US</a>

<footer class="abs footer">
  <div class="brand"><span class="brand-mark"></span><span class="brand-name">青葉木材株式会社</span></div>
  <p class="copyright">© 2021 AOBA TIMBER All rights reserved.</p>
</footer>

</body>
</html>
```